business card for author of crime novel

I am an author with a new book. I need a business card with the book's cover on one side (already uploaded), and contact details on the other.

Tom Velasquin
Author

telephone: 917-555-0162
website: www.tomvelasquin.example
facebook: friendsnet.example/tvelasquin
twitter: chirper.example/tvelasquin
email: tvelasquin@mailbox.example

Target Market(s)

Readers of mystery books

Industry/Entity Type

Business

Contact Information for Business Card

Tom Velasquin
Author

telephone: 917-555-0162

Font styles to use
Serif
Sans Serif

Requirements
Must have
• Book cover on one side. My contact info on the other, with the name of the book repeated if that makes sense. Clean design.
Should not have
• Overly ornate, too formal, too distracting

```html
<!DOCTYPE html>
<html lang="en">
<head>
<meta charset="utf-8">
<title>Tom Velasquin – Author Business Card</title>
<link rel="stylesheet" href="https://fonts.googleapis.com/css2?family=Lato:wght@400;700&family=PT+Serif:ital,wght@0,400;0,700;1,400&display=swap">
<style>
  :root {
    --stage: #2b2421;
    --card-black: #141414;
    --gold: #e0a53c;
    --cover-gold: #c9922a;
    --white: #f2f2f2;
    --ink: #111111;
    --parchment: #ecdcb4;
    --parchment-edge: #b89a5e;
    --photo-light: #7d98a8;
    --photo-mid: #46606f;
    --photo-dark: #1f2d38;
    --author-yellow: #e6c23a;
  }
  * { box-sizing: border-box; margin: 0; padding: 0; }
  html, body {
    width: 1200px; height: 844px; overflow: hidden;
    background: var(--stage);
  }
  .canvas {
    position: relative; width: 1200px; height: 844px;
    display: flex; align-items: center; justify-content: center; gap: 70px;
  }
  .card {
    position: relative;
    border-radius: 3px;
    box-shadow: 0 10px 28px rgba(0,0,0,.45);
    overflow: hidden;
    flex: none;
  }

  /* Contact side */
  .card--contact {
    width: 560px; height: 320px;
    background: var(--card-black);
    font-family: "Lato", Arial, sans-serif;
    color: var(--white);
  }
  .identity {
    position: absolute; left: 56px; top: 140px;
  }
  .identity__name {
    color: var(--gold); font-size: 22px; font-weight: 400; line-height: 1.1;
  }
  .identity__role {
    font-size: 15px; margin-top: 6px; margin-left: 16px;
  }
  .details {
    position: absolute; left: 250px; top: 66px;
    font-size: 15px; line-height: 1.36;
  }
  .details__address { margin-bottom: 16px; }
  .details__row { display: flex; gap: 8px; white-space: nowrap; }
  .details__key { color: var(--gold); width: 14px; }
  .details__web {
    color: var(--gold); margin-top: 16px; margin-left: 22px;
  }

  /* Cover side (portrait book cover) */
  .card--cover {
    width: 320px; height: 560px;
    background: var(--cover-gold);
    font-family: "PT Serif", Georgia, serif;
  }
  .cover__photo {
    position: absolute; left: 22px; top: 22px; right: 22px; height: 440px;
    background: linear-gradient(160deg, var(--photo-light) 0%, var(--photo-mid) 50%, var(--photo-dark) 100%);
  }
  .cover__series {
    position: absolute; left: 12px; top: 14px; right: 12px; height: 34px;
    background: var(--parchment);
    border: 1px solid var(--parchment-edge);
    display: flex; align-items: center; justify-content: center;
    font-style: italic; font-size: 18px; color: var(--ink);
  }
  .cover__author {
    position: absolute; left: 40px; top: 66px;
    color: var(--author-yellow); font-size: 17px; letter-spacing: 2px;
    line-height: 1.2; text-transform: uppercase;
  }
  .cover__title {
    position: absolute; left: 0; right: 0; bottom: 30px;
    text-align: center; font-weight: 700; font-size: 25px;
    letter-spacing: 2px; color: var(--ink); text-transform: uppercase;
    white-space: nowrap;
  }
</style>
</head>
<body>
<main class="canvas">
  <section class="card card--contact" aria-label="Contact side">
    <div class="identity">
      <p class="identity__name">Tom Velasquin</p>
      <p class="identity__role">Author</p>
    </div>
    <div class="details">
      <p class="details__address">12345, Address Goes Here<br>Country Name, 123456.</p>
      <p class="details__row"><span class="details__key">T:</span><span>917-555-0162</span></p>
      <p class="details__row"><span class="details__key">E:</span><span>tvelasquin@mailbox.example</span></p>
      <p class="details__row"><span class="details__key">f:</span><span>friendsnet.example/tvelasquin</span></p>
      <p class="details__row"><span class="details__key">t:</span><span>chirper.example/tvelasquin</span></p>
      <p class="details__web">www.tomvelasquin.example</p>
    </div>
  </section>

  <section class="card card--cover" aria-label="Book cover side">
    <div class="cover__photo" role="img" aria-label="Blue-toned photograph of an old apartment building facade with fire escapes, seen from below"></div>
    <p class="cover__series">A Marlowe Keane Mystery</p>
    <p class="cover__author">Tom<br>Velasquin</p>
    <h1 class="cover__title">Dead Drop Alley</h1>
  </section>
</main>
</body>
</html>
```